Cocktail Syrup / Mixers. Modern clean professional

Looking to design a line of cocktail syrups. The goal would have it look high end. Flavors include Pina Colada, Blue Hawaiian, Margaretta, and other fruit flavors. Labels should be hip, and modern looking. I attached the coffee blends as an example but would like it to be very different from these.

Target Market(s)

18-30

Industry/Entity Type

Food Production

Font styles to use
Serif
Sans Serif

Colors

Designer to choose colors to be used in the design.

Requirements
Must have
• Logo must be centered with the name of the flavor. The label size is 5" height, 8" wide.
Nice to have
• Fruit or some sort of design including different colors per label.
Should not have
• open to everything

```html
<!DOCTYPE html>
<html lang="en">
<head>
<meta charset="utf-8">
<title>Rooftop Syrups – Pina Colada Label</title>
<link rel="stylesheet" href="https://fonts.googleapis.com/css2?family=Fredoka:wght@600;700&family=Quicksand:wght@500;600&family=Roboto:wght@400;700&display=swap">
<style>
  :root {
    --backdrop: #d8d2cc;
    --paper: #ffffff;
    --ink: #1e1a1a;
    --ink-soft: #4a4a4a;
    --red: #e2141b;
    --red-deep: #d70f1a;
    --orange: #f0731e;
    --orange-warm: #ee5a1f;
    --leaf: #3aa53f;
    --navy: #23357a;
    --map-grey: #d9d9d9;
  }
  * { box-sizing: border-box; margin: 0; padding: 0; }
  html, body { width: 1200px; height: 868px; overflow: hidden; }
  body { background: var(--backdrop); position: relative; }

  .label {
    position: absolute; left: 40px; top: 115px;
    width: 1120px; height: 637px;
    background: var(--paper);
    overflow: hidden;
  }

  /* top band */
  .nutrition {
    position: absolute; left: 34px; top: 18px; width: 208px; height: 248px;
    border: 2px solid var(--ink-soft); padding: 5px 7px;
    font-family: "Roboto", sans-serif; color: var(--ink-soft);
  }
  .nutrition h2 { font-size: 19px; font-weight: 700; line-height: 1; }
  .nutrition .serving { font-size: 8.5px; font-weight: 700; line-height: 1.25; border-bottom: 5px solid var(--ink-soft); padding: 2px 0 3px; }
  .nutrition .amount { font-size: 8px; text-align: center; border-bottom: 1px solid var(--ink-soft); padding: 3px 0 2px; }
  .nutrition .calories { display: flex; justify-content: space-between; align-items: flex-end; font-size: 14px; font-weight: 700; border-bottom: 3px solid var(--ink-soft); padding: 2px 0; }
  .nutrition .calories small { display: block; font-size: 5px; font-weight: 400; text-align: right; }
  .nutrition ul { list-style: none; font-size: 8.5px; font-weight: 700; }
  .nutrition li { display: flex; justify-content: space-between; border-bottom: 1px solid #9a9a9a; padding: 2px 0; }
  .nutrition li:last-child { border-bottom: 4px solid var(--ink-soft); }
  .nutrition .footnote { font-size: 5.5px; line-height: 1.3; padding-top: 4px; }

  .brand {
    position: absolute; left: 384px; top: 30px; width: 360px;
    display: flex; flex-direction: column; align-items: center;
  }
  .brand-dot { width: 96px; height: 96px; border-radius: 50%; background: var(--ink); }
  .brand-name {
    margin-top: 40px;
    font-family: "Fredoka", sans-serif; font-weight: 700;
    font-size: 44px; line-height: 1; color: var(--ink); letter-spacing: 0.5px;
  }

  .story {
    position: absolute; left: 897px; top: 28px; width: 165px;
    font-family: "Quicksand", sans-serif; font-weight: 500;
    font-size: 10px; line-height: 1.35; color: var(--ink);
  }
  .story p + p { margin-top: 12px; }

  /* red band */
  .flavor-band {
    position: absolute; left: 0; top: 281px; width: 1120px; height: 337px;
    background: linear-gradient(100deg, var(--orange) 0%, var(--orange-warm) 30%, var(--red) 65%, var(--red-deep) 100%);
    overflow: hidden;
  }
  .flavor-band svg.waves { position: absolute; inset: 0; }

  .flavor {
    position: absolute; left: 0; right: 0; top: 148px; text-align: center; color: var(--paper);
  }
  .flavor h1 {
    font-family: "Fredoka", sans-serif; font-weight: 700;
    font-size: 64px; line-height: 1; letter-spacing: 1px;
  }
  .flavor .type { margin-top: 16px; font-family: "Roboto", sans-serif; font-size: 20px; line-height: 1.15; }
  .flavor .volume { font-family: "Roboto", sans-serif; font-size: 19px; line-height: 1.2; }
  .flavor .volume b { font-weight: 700; }

  .ingredients {
    position: absolute; left: 34px; top: 198px; width: 230px;
    font-family: "Roboto", sans-serif; font-size: 12.5px; line-height: 1.3; color: var(--paper);
  }
  .ingredients b { font-weight: 700; }

  .badges {
    position: absolute; left: 937px; top: 12px; width: 96px;
    display: flex; flex-direction: column; align-items: center;
  }
  .badge-natural { width: 40px; height: 40px; border-radius: 50%; background: var(--leaf); }
  .badge-state { margin-top: 12px; width: 52px; height: 54px; background: var(--map-grey); border-radius: 8px 14px 6px 10px; }
  .badge-state-text {
    margin-top: 4px; font-family: "Roboto", sans-serif; font-weight: 700;
    font-size: 10px; line-height: 1.1; color: var(--paper); text-align: center;
  }
  .badge-flag { margin-top: 18px; width: 92px; height: 50px; background: var(--navy); border: 2px solid var(--paper); }

  .maker {
    position: absolute; left: 919px; top: 262px;
    font-family: "Roboto", sans-serif; font-weight: 700;
    font-size: 11.5px; line-height: 1.3; color: var(--paper);
  }
</style>
</head>
<body>
  <main class="label">
    <section class="nutrition" aria-label="Nutrition facts">
      <h2>NUTRITION FACTS</h2>
      <p class="serving">25 serving per container<br>Serving size 1 oz (28,4 g)</p>
      <p class="amount">Amount per serving</p>
      <div class="calories"><span>Calories</span><span>60<small>% daily value</small></span></div>
      <ul>
        <li><span>Total fat 0g</span><span>0%</span></li>
        <li><span>Saturated fat 0g</span><span>0%</span></li>
        <li><span>Trans fat 0g</span><span>0%</span></li>
        <li><span>Soduim 0g</span><span>0%</span></li>
        <li><span>Total Carbohydrate 16 g</span><span>6%</span></li>
        <li><span>Dietary fiber 0g</span><span>0%</span></li>
        <li><span>Total sugar 16 g</span><span>6%</span></li>
        <li><span>Protein 0g</span><span>0%</span></li>
      </ul>
      <p class="footnote">Not a significant source of cholesterol, vitamin D, calcium, iron and potassium.<br>* The % Daily value (DV) tells you how much a nutrient in a serving of food contributes to a daily diet. 2,000 calories a day is used for general nutrition advice.</p>
    </section>

    <div class="brand">
      <span class="brand-dot"></span>
      <span class="brand-name">ROOFTOP SYRUPS</span>
    </div>

    <div class="story">
      <p>Rooftop Syrups are small batch gourmet craft syrups. We formulate each authentic flavor to the highest standards using only the finest natural ingredients. We use only natural sweeteners like real sugar, and sucralose for our sugar free syrups. Rooftop Syrups is flavorful, natural, and sophisticated.</p>
      <p>Rooftop Syrups are perfect to add a unique flavor to any beverage, dessert, ice cream, coffee, shakes and more. The recipes are endless! I hope you enjoy these as much we do!</p>
    </div>

    <section class="flavor-band">
      <svg class="waves" width="1120" height="337" viewBox="0 0 1120 337" aria-hidden="true">
        <path d="M0 0 H1120 V40 C1060 20 1010 70 960 60 C900 48 880 -5 800 10 C740 22 720 60 640 50 C560 40 540 -10 440 5 C360 18 300 70 200 80 C120 88 60 60 0 95 Z" fill="#ffffff" opacity="0.0"/>
        <path d="M0 70 C80 40 160 20 240 25 C330 30 360 -5 470 0 L700 0 C760 0 770 40 830 45 C870 48 880 70 920 110 L920 0 L0 0 Z" fill="var(--orange)" opacity="0.55"/>
        <path d="M640 0 C660 50 700 60 720 90 C740 120 780 110 790 80 C800 50 840 40 860 10 L860 0 Z" fill="var(--orange)" opacity="0.8"/>
        <path d="M0 280 C120 250 250 300 380 285 C480 272 520 245 640 255 C720 262 760 300 840 290 C900 282 940 250 1000 260 L1000 337 L0 337 Z" fill="var(--red-deep)" opacity="0.75"/>
        <circle cx="290" cy="95" r="18" fill="var(--red-deep)"/>
        <circle cx="345" cy="125" r="6" fill="var(--red-deep)"/>
        <circle cx="852" cy="150" r="14" fill="var(--orange)" opacity="0.8"/>
      </svg>

      <div class="flavor">
        <h1>PINA COLADA</h1>
        <p class="type">FALORED SYRUP</p>
        <p class="volume">25.35 fl Oz <b>(750 ml)</b></p>
      </div>

      <p class="ingredients"><b>INGREDIENTS</b>: WATER, SUGAR, CITRIC ACID, NATURAL FLAVOUR, SODUIM BENZOATE (PRESSERVATIVE)</p>

      <div class="badges">
        <span class="badge-natural" role="img" aria-label="Natural ingredients badge"></span>
        <span class="badge-state" role="img" aria-label="State outline"></span>
        <span class="badge-state-text">PROUDLY<br>MADE IN<br>MICHIGAN</span>
        <span class="badge-flag" role="img" aria-label="Made in USA badge"></span>
      </div>

      <p class="maker">MANUFACTED BY:<br>BRIGHTWELL FLAVORS INC.<br>42 HARBOR STREET<br>LAKEPORT, MI 48059<br>WWW.ROOFTOPSYRUPS.COM</p>
    </section>
  </main>
</body>
</html>
```